Flyer-Design für Schamanismus-Pferde-Musik
Vielen Dank, es war eine tolle Zusammenarbeit, mit vielen kreativen Vorschlägen Seitens der Designerin und einer sehr schnellen, guten Umsetzung meiner Änderungswünsche!
Zielgruppe
Schamanismus-Pferde-Musik
schamanische Heilarbeit im grünen Haus ;-)
Einzel- und Gruppencoaching mit PFERD zur Persönlichkeitsentwicklung
Aufgabenstellung
ich persönlich finde quadratische Flyer sehr schön...

```html
<!DOCTYPE html>
<html lang="de">
<head>
<meta charset="utf-8">
<title>Flyer Schamanische Heilarbeit</title>
<link href="https://fonts.googleapis.com/css2?family=Dancing+Script:wght@700&family=Nunito+Sans:ital,wght@0,400;0,600;1,400&display=swap" rel="stylesheet">
<style>
  :root {
    --red: #b01818;
    --dark: #3a3a3c;
    --white: #ffffff;
    --label: #9a9a9a;
    --paper: #ffffff;
    --caption-bg: rgba(240,240,240,0.92);
    --script: "Dancing Script", cursive;
    --sans: "Nunito Sans", sans-serif;
  }
  html, body { margin: 0; padding: 0; overflow: hidden; }
  body { background: var(--paper); font-family: var(--sans); }
  .canvas { position: relative; width: 1200px; height: 855px; overflow: hidden; background: var(--paper); }

  .side-label { position: absolute; font-size: 9.5px; color: var(--label); transform: translateX(-50%); white-space: nowrap; }

  .strip { position: absolute; left: 55px; width: 1079px; height: 361px; box-shadow: 2px 3px 4px rgba(0,0,0,0.25); background: var(--white); }
  .strip::before, .strip::after { content: ""; position: absolute; left: 0; right: 0; background: var(--dark); }
  .strip::before { top: 0; height: 8px; border-bottom: 3px solid var(--red); }
  .strip::after { bottom: 0; height: 8px; border-top: 3px solid var(--red); }
  .strip--outer { top: 46px; }
  .strip--inner { top: 444px; }

  .panel { position: absolute; top: 11px; height: 339px; overflow: hidden; }
  .panel--red { background: var(--red); color: var(--white); }
  .panel--white { background: var(--white); color: #444; }

  .photo { position: absolute; }

  /* Cover inside */
  .cover-title { position: absolute; font-family: var(--script); font-weight: 700; color: var(--white); font-size: 52px; line-height: 1; text-shadow: 2px 3px 3px rgba(0,0,0,0.45); white-space: nowrap; }
  .caption-box { position: absolute; left: 120px; top: 296px; width: 218px; height: 24px; background: var(--caption-bg); font-size: 7.4px; color: #444; display: flex; align-items: center; justify-content: center; }

  /* Back */
  .contact { position: absolute; left: 0; right: 0; top: 264px; bottom: 0; border-top: 4px solid var(--white); background: var(--red); color: var(--white); text-align: center; }
  .contact__name { font-family: var(--script); font-weight: 700; font-size: 15px; margin-top: 14px; }
  .contact__line { font-size: 7.4px; line-height: 12.5px; }

  /* Front */
  .front-box { position: absolute; left: 176px; top: 294px; width: 184px; height: 45px; background: #ededed; text-align: center; }
  .front-box__title { font-family: var(--script); font-weight: 700; color: var(--red); font-size: 19px; margin-top: 6px; line-height: 1; }
  .front-box__sub { font-size: 7.4px; color: #444; margin-top: 2px; }

  /* Inner text */
  .heading { position: absolute; font-family: var(--script); font-weight: 700; font-size: 15px; line-height: 1; white-space: nowrap; }
  .heading--red { color: var(--red); }
  .copy { position: absolute; font-size: 7.4px; line-height: 12.35px; margin: 0; }
  .copy p { margin: 0 0 12.35px; }
  .copy--justify { text-align: justify; }
  .offer-list { list-style: none; margin: 0; padding: 0; }
  .offer-title { font-weight: 600; }
  .program { position: absolute; font-size: 7.4px; line-height: 10.5px; }
  .program__title { color: var(--red); font-size: 7.6px; }
  .program__target { font-size: 5.6px; font-style: italic; line-height: 9px; color: #555; text-align: justify; margin-bottom: 14px; }
  .program__target b { color: var(--red); font-style: normal; font-weight: 400; }
</style>
</head>
<body>
<div class="canvas">

  <span class="side-label" style="left:239px;top:17px;">1. Seite innen</span>
  <span class="side-label" style="left:593px;top:17px;">Rückseite</span>
  <span class="side-label" style="left:954px;top:17px;">Vorderseite</span>

  <section class="strip strip--outer">
    <!-- 1. Seite innen -->
    <div class="panel" style="left:0;width:358px;">
      <div class="photo" role="img" aria-label="Frau sitzt im moosigen Nadelwald und blickt nach oben" style="inset:0;background:linear-gradient(160deg,#6b5a6a 0%,#8a7d86 25%,#5f7a3a 55%,#7fa03c 80%,#4d6a2a 100%);"></div>
      <span class="cover-title" style="left:28px;top:34px;">„Die mit</span>
      <span class="cover-title" style="left:92px;top:100px;">der Geige</span>
      <span class="cover-title" style="left:200px;top:172px;">tanzt“</span>
      <div class="caption-box">bekannt durch die von ihr mitgegründete Band Nebelharfe</div>
    </div>

    <!-- Rückseite -->
    <div class="panel" style="left:358px;width:361px;">
      <div class="photo" role="img" aria-label="Abgeerntetes Getreidefeld vor bewaldetem Hügel mit grünem Haus" style="left:0;top:0;width:361px;height:264px;background:linear-gradient(180deg,#4f6a38 0%,#6c8446 45%,#c9ab64 62%,#e0c47e 100%);"></div>
      <div class="contact">
        <div class="contact__name">Birte Lena Hovsmann</div>
        <div class="contact__line">Lindenweg 7 • 94501 Waldheim (Bachtal) • Tel.: 0170 5550123</div>
        <div class="contact__line">Info &amp; Anmeldung unter: www.wald-ross-klang.de</div>
      </div>
    </div>

    <!-- Vorderseite -->
    <div class="panel" style="left:719px;width:360px;">
      <div class="photo" role="img" aria-label="Frau spielt Geige neben einem Schimmel" style="left:0;top:0;width:172px;height:126px;background:linear-gradient(135deg,#8c8478,#5a544c 60%,#a9a296);"></div>
      <div class="photo" role="img" aria-label="Frau mit Rahmentrommel und schwarzem Hund vor einem Stall" style="left:0;top:131px;width:172px;height:208px;background:linear-gradient(180deg,#6d625a,#7c7a78 55%,#9a948c);"></div>
      <div class="photo" role="img" aria-label="Frau mit Geige auf schwarzem Pferd im grünen Wald" style="left:176px;top:0;width:184px;height:294px;background:linear-gradient(160deg,#8fbf3a,#5b8a26 45%,#2c3a1c 80%,#1e1e1e);"></div>
      <div class="front-box">
        <div class="front-box__title">Schamanische Heilarbeit</div>
        <div class="front-box__sub">im grünen Haus</div>
      </div>
    </div>
  </section>

  <span class="side-label" style="left:237px;top:423px;">innen links</span>
  <span class="side-label" style="left:591px;top:423px;">innen mittig</span>
  <span class="side-label" style="left:952px;top:423px;">innen rechts</span>

  <section class="strip strip--inner">
    <!-- innen links -->
    <div class="panel panel--red" style="left:0;width:360px;">
      <h2 class="heading" style="left:19px;top:16px;margin:0;">Schamanische Heilarbeit</h2>
      <div class="copy copy--justify" style="left:19px;top:46px;width:101px;">
        <p>Schamanismus ist keine Religion, es ist eine Lebenseinstellung!</p>
        <p>Eins sein mit der Natur und allen Wesen um uns. Jeder Baum, jeder Stein, jedes Tier hat eine Seele. Auch unsere Ahnen spielen eine große Rolle.</p>
        <p>In der schamanischen Ansicht hängen Körper und Seele zusammen. Somit liegt die Lösung für unsere Beschwer&shy;den in unserem Inneren. Der Schamane verbindet sich mit der geistigen Welt und lässt seine heilenden Kräfte von dieser leiten.</p>
      </div>
      <div class="copy" style="left:132px;top:46px;width:218px;">
        <p class="offer-title">Heilarbeit, Angebot</p>
        <ul class="offer-list">
          <li>- Chakrenreinigung</li>
          <li>- Rückholung verlorener Seelenanteile</li>
          <li>- Reinigung mit Heilsteinen (Lira Omsen)</li>
          <li>- Heilarbeit mit Tieren</li>
          <li>- Hausreinigung (bei Ihnen Zuhause)</li>
          <li>- Schamanische Reisen</li>
          <li>- Arbeit mit Krafttieren</li>
          <li>- Persönlichkeitsentwicklung</li>
          <li>u.v.m. - &nbsp;je nach dem, was individuell ruft.</li>
        </ul>
        <p style="margin-top:12.35px;">Heilsitzungen sind auch aus der Ferne möglich! Dazu machen wir einen Termin aus, an dem Sie sich an einem ungestörten Ort Ihrer Wahl für ca. eine Stunde Zeit nehmen müssen.</p>
      </div>
      <h3 class="heading" style="left:132px;top:250px;margin:0;">Monatliche Veranstaltungen:</h3>
      <div class="copy" style="left:132px;top:270px;width:218px;">Naturtage, Rauhnachtszeremonie, Feuerzeremonie, Vollmond&shy;trommeln, Frauenkreise…</div>
    </div>

    <!-- innen mittig -->
    <div class="panel panel--white" style="left:360px;width:361px;">
      <h2 class="heading heading--red" style="left:14px;top:16px;margin:0;">Pferdegestützte Persönlichkeitsentwicklung</h2>
      <div class="copy copy--justify" style="left:15px;top:46px;width:217px;">
        <p><i>KEINE</i> Reiterfahrung oder Pferdekenntnis notwendig. Wir machen alle Übungen vom Boden aus!</p>
        <p>Pferde sind die Spiegel unserer Seele. Wenn wir authentisch sind, wird ein Pferd mit uns freiwillig Kontakt aufnehmen. Diese wunderbaren, kraftvollen Wesen helfen uns, innerste Wünsche aufzudecken, Trauer zu verarbeiten, Kraft zu tanken und wahrhaftige Kommunikation wieder zu erlernen – die nichts mit "viel reden" zu tun hat…</p>
      </div>
      <div class="photo" role="img" aria-label="Sepiabild: Hand berührt das Maul eines hellen Pferdes" style="left:244px;top:18px;width:102px;height:136px;background:linear-gradient(135deg,#efe8de,#c9b79f 50%,#5a3f2c);"></div>
      <div class="photo" role="img" aria-label="Frau streichelt ein weißes Pony auf der Weide" style="left:15px;top:168px;width:217px;height:171px;background:linear-gradient(160deg,#4e6e2c,#7c9a4a 40%,#d8d6cf 65%,#6d7a5c);"></div>
      <div class="program" style="left:244px;top:170px;width:102px;">
        <div class="program__title">"Sprenge Deine Grenzen &amp; Lebe Deinen Traum!"</div>
        <div class="program__target"><b>Zielgruppe:</b> Privatpersonen, die etwas in ihrem Leben verändern wollen, aber noch nach dem Weg dahin suchen.</div>
        <div class="program__title">"Baue Dein Team"</div>
        <div class="program__target"><b>Zielgruppe:</b> Gruppen jeglicher Art, ob Jugendgruppen, Bands, Gemein&shy;schaften, Familien etc.</div>
        <div class="program__title">"Die Kunst des Führens"</div>
        <div class="program__target"><b>Zielgruppe:</b> Führungskräfte in Firmen, Lehrer, Mütter – alle, die eine Gruppe zu leiten haben.</div>
      </div>
    </div>

    <!-- innen rechts -->
    <div class="panel panel--red" style="left:721px;width:185px;">
      <h2 class="heading" style="left:14px;top:16px;margin:0;">Feedback</h2>
      <div class="copy" style="left:14px;top:45px;width:160px;">
        <p>"Es war genau das was ich gebraucht hab! Hab danach einiges im Leben geändert, wozu mir sonst immer der Mut, die Kraft und Energie gefehlt hat! Ich habe einen neuen Job ab August, genau das, was ich gesucht hab! Ich wohne jetzt in einer neuen kleinen Wohnung! Fühle mich richtig gut! Manchmal braucht man einfach wirklich nur eine Auszeit, um Ruhe und Kraft zu tanken! Danke dafür und ganz besonders für die Flussreise!"</p>
        <p>"Mir hat die Möglichkeit mich so unbefan&shy;gen den Pferden zu nähern die schönsten Erfahrungen gebracht. Das dauert bis ich alles verstanden habe, aber es tat sehr gut und ich schöpfe Kraft daraus."</p>
        <p>"Bei Dir konnte ich loslassen und voran&shy;schreiten – saugut! Eine tolle Erfahrung."</p>
      </div>
    </div>
    <div class="panel panel--white" style="left:906px;width:173px;">
      <div class="photo" role="img" aria-label="Frau mit geschlossenen Augen wird von mehreren Händen gestützt, im Freien" style="left:3px;top:0;width:170px;height:238px;background:linear-gradient(160deg,#b9c4c8,#8a8a5e 45%,#3c4258 70%,#7f8a5a);"></div>
      <div class="photo" role="img" aria-label="Hände halten eine Feder mit Perlenband" style="left:3px;top:243px;width:170px;height:96px;background:linear-gradient(135deg,#6a7a8e,#a6552a 50%,#3f5070);"></div>
    </div>
  </section>

</div>
</body>
</html>
```